Stretch on the Green with Mira

I want to advertise my Stretch on the Green classes for Summer. Classes are outside at The Sunny Corner Park. Holloway field. 83 Marangi St. Kelvindale.
Classes are for beginners to advance levels.
Classes start Monday, October 17th.
Monday 6pm Beginners
Tuesday 6pm Intermediate
Thursday 6pm Intermediate/Advance
Saturday 9am All fitness levels
My Pilates classes are specially designed to help improve strength and flexibility but as well will also improve posture, reduce stress and develop control and endurance in the entire body.
Booking essential. Limited numbers so I can make sure the correct technique is always being followed.
For more info or to book contact details:
Mira 027358164
mira@corewithmira.net
www.corewithmira.net
$15 Per Session

Target Market(s)

Males and Females ages 35plus.

Industry/Entity Type

Fitness

Font styles to use
Sans Serif

Requirements
Must have
• My logo. Contact details. A Park that looks lovely to exercise at.
Nice to have
• Summer looking. Trees - inspiration to be exercising outside

```html
<!DOCTYPE html>
<html lang="en">
<head>
<meta charset="utf-8">
<title>Stretch on the Green with Mira</title>
<link rel="stylesheet" href="https://fonts.googleapis.com/css2?family=Open+Sans:wght@400;600;700&family=Tinos:wght@400;700&display=swap">
<style>
:root{
  --bg:#eef6f8;
  --cream:#f8efea;
  --green:#17695a;
  --pink:#ee86b4;
  --pink-deep:#e56ea6;
  --teal:#5cc3c3;
  --teal-deep:#3aa8ab;
  --charcoal:#3a3d3e;
  --text:#3b3b3b;
  --white:#ffffff;
}
*{margin:0;padding:0;box-sizing:border-box}
html,body{width:1200px;height:2374px;overflow:hidden;background:var(--bg)}
.flyer{position:absolute;left:50px;top:410px;width:785px;height:1110px;background:var(--cream);transform:scale(1.4);transform-origin:top left;overflow:hidden;font-family:"Open Sans",Arial,sans-serif;color:var(--text)}
.photo{position:absolute;left:0;top:0;width:785px;height:600px;background:linear-gradient(160deg,#8fb65a 0%,#6e9a3e 45%,#5d8434 100%)}
.waves{position:absolute;left:0;top:400px;width:785px;height:240px}
.price{position:absolute;left:40px;top:478px;color:var(--white);display:flex;align-items:center;gap:8px}
.price-amount{font-family:"Tinos","Times New Roman",serif;font-weight:700;font-size:82px;line-height:1}
.price-unit{font-weight:700;font-size:30px;line-height:1.05;letter-spacing:.5px}
.brand{position:absolute;left:520px;top:584px;display:flex;align-items:center;gap:10px}
.brand-dot{width:16px;height:16px;border-radius:50%;background:var(--pink);flex:none}
.brand-name{font-family:"Tinos","Times New Roman",serif;font-weight:400;font-size:24px;line-height:1;color:var(--green);white-space:nowrap}
.headline{position:absolute;left:44px;top:646px;font-family:"Tinos","Times New Roman",serif;font-weight:400;font-size:46px;line-height:52px;color:var(--green)}
.schedule{position:absolute;left:44px;top:770px;border-left:4px solid var(--pink);padding-left:16px}
.schedule-title{font-family:"Tinos","Times New Roman",serif;font-weight:700;font-size:20px;line-height:24px;color:var(--green)}
.schedule-list{list-style:none;margin-top:8px}
.schedule-list li{font-size:13px;line-height:22px;display:flex;align-items:center;gap:6px}
.tick{width:11px;height:11px;flex:none}
.about{position:absolute;left:427px;top:772px;width:316px;font-size:12.5px;line-height:18px;text-align:justify}
.venue{position:absolute;left:427px;top:850px;width:316px;text-align:center}
.venue-rule{display:flex;align-items:center;gap:6px}
.venue-rule span{flex:1;height:1px;background:#9a9a9a}
.venue-name{font-family:"Tinos","Times New Roman",serif;font-weight:400;font-size:33px;line-height:36px;color:var(--green);margin-top:2px;white-space:nowrap}
.venue-address{font-size:15px;color:var(--pink);line-height:20px;white-space:nowrap}
.venue-bottom{height:1px;background:#9a9a9a;margin-top:4px}
.water{position:absolute;left:0;top:950px;width:785px;height:135px;background:linear-gradient(180deg,var(--teal) 0%,var(--teal-deep) 55%,var(--teal) 100%)}
.base-band{position:absolute;left:0;top:1085px;width:785px;height:25px;background:var(--pink)}
.booking{position:absolute;left:44px;top:982px;border-left:3px solid var(--green);padding-left:20px}
.booking-title{font-family:"Tinos","Times New Roman",serif;font-weight:700;font-size:27px;line-height:30px;color:var(--green)}
.booking-text{font-size:14px;line-height:20px;color:#2f3b3b}
.contact{position:absolute;left:399px;top:977px;width:386px;height:95px;background:var(--charcoal);color:var(--white);padding:10px 18px}
.contact-lead{font-family:"Tinos","Times New Roman",serif;font-weight:700;font-size:15px;border-bottom:1px solid #8c8c8c;padding-bottom:4px}
.contact-lead em{font-style:normal;color:var(--pink)}
.contact-row{display:flex;align-items:center;margin-top:10px}
.phone{display:flex;align-items:center;gap:8px;font-weight:700;font-size:23px;padding-right:10px;border-right:1px solid #8c8c8c}
.phone svg{width:20px;height:20px}
.links{padding-left:8px;font-size:10.5px;line-height:15px}
.links b{color:var(--pink);font-weight:600}
.links i{display:inline-block;width:6px;height:6px;border-radius:50%;background:#9a9a9a;margin-right:4px;vertical-align:middle}
</style>
</head>
<body>
<main class="flyer">
  <div class="photo" role="img" aria-label="Photo of a small group sitting cross-legged on mats on a sunny park lawn, dappled tree shade"></div>

  <svg class="waves" viewBox="0 0 785 240" aria-hidden="true">
    <path d="M0 62 C120 20 240 40 340 80 C430 118 520 160 610 150 C690 140 750 90 785 50 V240 H0 Z" fill="var(--green)"/>
    <path d="M0 74 C120 34 240 54 340 94 C430 130 520 172 610 162 C690 152 750 104 785 66 V240 H0 Z" fill="var(--cream)"/>
    <path d="M0 76 C110 40 230 52 330 92 C380 112 410 130 430 140 C370 170 280 200 170 210 C90 216 30 205 0 190 Z" fill="var(--pink)"/>
    <path d="M0 180 C40 200 100 212 170 210 C280 206 370 176 430 140 C380 180 280 218 170 222 C90 225 30 212 0 196 Z" fill="var(--pink-deep)"/>
  </svg>

  <div class="price">
    <span class="price-amount">$15</span>
    <span class="price-unit">PER<br>SESSION</span>
  </div>

  <div class="brand">
    <span class="brand-dot"></span>
    <span class="brand-name">Stretch with Mira</span>
  </div>

  <h1 class="headline">Classes are for beginners<br>to advance levels.</h1>

  <section class="schedule">
    <h2 class="schedule-title">Classes start<br>Monday, October 17th</h2>
    <ul class="schedule-list">
      <li><svg class="tick" viewBox="0 0 12 12"><circle cx="6" cy="6" r="6" fill="var(--green)"/><path d="M3.3 6.2 5.2 8 8.8 4.2" stroke="#fff" stroke-width="1.6" fill="none"/></svg>Monday 6pm Beginners</li>
      <li><svg class="tick" viewBox="0 0 12 12"><circle cx="6" cy="6" r="6" fill="var(--green)"/><path d="M3.3 6.2 5.2 8 8.8 4.2" stroke="#fff" stroke-width="1.6" fill="none"/></svg>Tuesday 6pm Intermediate</li>
      <li><svg class="tick" viewBox="0 0 12 12"><circle cx="6" cy="6" r="6" fill="var(--green)"/><path d="M3.3 6.2 5.2 8 8.8 4.2" stroke="#fff" stroke-width="1.6" fill="none"/></svg>Thursday 6pm Intermediate/Advance</li>
      <li><svg class="tick" viewBox="0 0 12 12"><circle cx="6" cy="6" r="6" fill="var(--green)"/><path d="M3.3 6.2 5.2 8 8.8 4.2" stroke="#fff" stroke-width="1.6" fill="none"/></svg>Saturday 9am All fitness levels</li>
    </ul>
  </section>

  <p class="about">My Pilates classes are specially designed to help improve strength and flexibility but as well will also improve posture, reduce stress and develop control and endurance in the entire body.</p>

  <section class="venue">
    <div class="venue-rule"><span></span>
      <svg width="14" height="18" viewBox="0 0 14 18"><path d="M7 0C3.1 0 0 3 0 6.8 0 11.5 7 18 7 18s7-6.5 7-11.2C14 3 10.9 0 7 0z" fill="var(--pink)"/><circle cx="7" cy="6.8" r="2.6" fill="var(--cream)"/></svg>
    <span></span></div>
    <h2 class="venue-name">The Sunny Corner Park</h2>
    <p class="venue-address">Holloway field. 83 Marangi St. Kelvindale.</p>
    <div class="venue-bottom"></div>
  </section>

  <div class="water" role="img" aria-label="Calm turquoise water surface"></div>
  <div class="base-band"></div>

  <section class="booking">
    <h2 class="booking-title">Booking essential</h2>
    <p class="booking-text">Limited numbers so I can make sure the<br>correct technique is always being followed</p>
  </section>

  <section class="contact">
    <p class="contact-lead">For more info or to book contact details: <em>Mira</em></p>
    <div class="contact-row">
      <span class="phone">
        <svg viewBox="0 0 20 20"><circle cx="10" cy="10" r="10" fill="var(--pink)"/><path d="M7 5.2c.4-.3.9-.2 1.1.2l1 1.8c.2.4.1.8-.2 1.1l-.7.6c.5 1.2 1.4 2.2 2.6 2.8l.6-.7c.3-.3.8-.4 1.1-.2l1.8 1c.4.2.5.7.2 1.1l-.8 1c-.5.6-1.3.8-2 .5-2.7-1.1-4.7-3.2-5.7-5.8-.3-.7-.1-1.5.5-2z" fill="#fff"/></svg>
        027358164
      </span>
      <div class="links">
        <div><i></i>www.<b>corewithmira</b>.net</div>
        <div><i></i>mira@<b>corewithmira</b>.net</div>
      </div>
    </div>
  </section>
</main>
</body>
</html>
```